Lend a Lantern Website Design (design layout only)

We need a website design for a new nonprofit organization based in Des Moines, Iowa called Lend a Lantern. The nonprofit provides soccer training opportunities to youth soccer players looking to improve their game while also affecting the lives of the less fortunate in a positive way. While participating in the training programs the players also go out and raise money for selected charities. The organization then donates the funds. In its first 18 months we donated $10,500. We would like to see designs attempt to symbolize the mission of the nonprofit - essentially "improve you while improving someone else."

We would like to see the following features:

· A place to donate - Our intent is to have the home page linked to the donation page; a simple straight-forward process for people to give money, and make donating as painless as possible - no account needed to make a donation, credit card or e-check should be the only information needed to donate, and have it be on a single page.

· A photo gallery so people can browse the photo gallery to get a better understanding of our organization and a place to add videos and a calendar to show upcoming events

· A place for contact information and the profiles of directors and board members. This should include a spot showing all the charities the organization donates to. Also includes a news section/blog for comments and suggestions.

We want the design to revolve around the content and mission. We would really like to stress our organization as nonprofit. We would also like if the website was user friendly and easy to navigate.

The logo of our organization is uploaded

```html
<!DOCTYPE html>
<html lang="en">
<head>
<meta charset="utf-8">
<title>Lend a Lantern</title>
<link rel="stylesheet" href="https://fonts.googleapis.com/css2?family=Bitter:ital,wght@0,400;0,700;1,400&family=Arimo:wght@400;700&display=swap">
<style>
:root{
  --green:#7b9f4f;
  --green-light:#8fb062;
  --green-dark:#4b6b2c;
  --green-deep:#3f5a25;
  --grey:#8b8b8b;
  --text:#555;
  --line:#c9c9c9;
  --white:#fff;
}
*{box-sizing:border-box;margin:0;padding:0}
html,body{width:878px;height:1200px;overflow:hidden;background:var(--white)}
body{position:relative;font-family:"Arimo",Arial,sans-serif;color:var(--text)}
.abs{position:absolute}

/* header */
.brand{left:122px;top:62px;display:flex;align-items:center;gap:6px;font-family:"Bitter",Georgia,serif;font-weight:700;font-size:17px;color:var(--green-dark)}
.brand-dot{width:14px;height:14px;border-radius:50%;background:var(--green)}
.btn-donate{background:var(--green-dark);color:var(--white);font-family:"Bitter",Georgia,serif;font-weight:700;font-size:13px;letter-spacing:.5px;border-radius:4px;display:flex;align-items:center;justify-content:center;box-shadow:1px 2px 2px rgba(0,0,0,.3);white-space:nowrap}
.header-donate{left:648px;top:21px;width:110px;height:26px}
.phone{left:636px;top:58px;display:flex;align-items:center;gap:6px;font-size:16px;color:var(--green-deep);font-weight:700}
.nav{left:352px;top:89px;display:flex;gap:13px;font-size:11px;color:#333;white-space:nowrap}
.nav .current{color:var(--green-dark)}

/* hero */
.hero-band{left:0;top:116px;width:878px;height:307px;background:var(--green)}
.hero-photo{left:118px;top:116px;width:645px;height:307px;background:linear-gradient(135deg,#5d6e86 0%,#9aa3ab 40%,#c9b8a6 60%,#3f3f3f 100%)}
.hero-caption{left:118px;top:397px;width:645px;height:26px;background:rgba(0,0,0,.45);color:var(--white);font-family:"Bitter",Georgia,serif;font-size:14px;letter-spacing:.4px;padding:4px 5px;white-space:nowrap}
.hero-dots{right:10px;top:9px;display:flex;gap:3px}
.hero-dots i{width:5px;height:5px;border-radius:50%;background:#bbb;display:block}

/* welcome */
.h2{font-family:"Bitter",Georgia,serif;font-weight:700;font-size:17px;color:var(--green);white-space:nowrap}
.h2 .muted{color:var(--grey)}
.h2 .dark{color:var(--green-dark)}
.welcome-title{left:118px;top:437px}
.welcome-text{left:118px;top:463px;width:412px;font-size:9.1px;line-height:11.7px;color:#666}
.welcome-text b{color:var(--green-dark)}
.mission{left:117px;top:554px;width:415px;font-family:"Bitter",Georgia,serif;font-style:italic;font-size:10.3px;line-height:13.6px;color:#666}
.video-title{left:548px;top:438px;font-size:14px}
.video{left:548px;top:463px;width:211px;height:132px;border:1px solid #999;background:linear-gradient(120deg,#d8cfc2,#c34a3c 55%,#e8d8c8)}
.video-bar{position:absolute;left:0;bottom:0;width:100%;height:20px;background:#222;border-top:3px solid #c21d1d}
.video-play{position:absolute;left:91px;top:44px;width:26px;height:26px;border-radius:50%;background:rgba(0,0,0,.7)}

/* gallery */
.gallery{left:122px;top:617px;width:633px;height:149px;border:2px solid #a9bf8f;border-radius:8px}
.gallery-title{left:128px;top:620px;font-size:14px}
.gallery-arrows{left:722px;top:620px;font-size:14px;color:#333;letter-spacing:4px}
.thumb{top:646px;width:121px;height:101px;background:var(--white);border:1px solid #ddd;padding:4px;box-shadow:0 3px 4px rgba(0,0,0,.25)}
.thumb div{width:100%;height:100%}

/* tabs */
.tab{top:794px;height:21px;font-family:"Bitter",Georgia,serif;font-size:9.5px;line-height:12px;padding:5px 0 0;text-align:center;white-space:nowrap;overflow:hidden;border:1px solid var(--line);border-bottom:none;background:#fafafa;color:#444}
.tab.on{background:var(--green);color:#222;border-color:var(--green)}
.panel{border:2px solid var(--green);background:var(--white)}
.news{left:118px;top:815px;width:272px;height:172px;padding:9px 10px 0}
.news-item{font-size:8.4px;line-height:11px;color:#555;padding-bottom:4px;margin-bottom:5px;border-bottom:1px solid #eee}
.news-item:last-of-type{border:none;margin:0;padding:0}
.news-item .date{color:var(--green-deep);font-size:7.5px;line-height:10px}
.dots{position:absolute;bottom:4px;right:22px;display:flex;gap:3px}
.dots i{width:5px;height:5px;border-radius:50%;background:#ccc;display:block}
.dots i:first-child{background:var(--green-dark)}
.directors{left:401px;top:815px;width:194px;height:172px;padding:10px 10px}
.person{display:flex;gap:10px;margin-bottom:9px}
.avatar{width:42px;height:42px;border:1px solid #666;background:linear-gradient(#6f7f95,#2f3a4f)}
.person p{font-size:8.4px;line-height:12px;color:#666}
.person .name{font-family:"Bitter",Georgia,serif;font-size:9px;color:#666}

/* support */
.support-title{left:608px;top:794px;width:149px;height:26px;border:1px solid var(--line);border-bottom:none;font-family:"Bitter",Georgia,serif;font-weight:700;font-size:11.5px;color:#666;padding:6px 0 0 6px;white-space:nowrap}
.support{left:605px;top:820px;width:154px;height:66px;background:var(--green);color:var(--white);text-align:center;font-size:10px;font-weight:700;line-height:12px;padding-top:7px;border-radius:0 0 3px 3px}
.support .btn-donate{width:106px;height:20px;margin:6px auto 0;font-size:12px;background:var(--green-deep)}
.support-shadow{left:608px;top:886px;width:149px;height:7px;background:#e6e6e6}
.follow{left:608px;top:904px;width:147px;height:83px;background:linear-gradient(#4d6a30,#3b5524);color:var(--white);padding:6px}
.follow h3{font-size:13px;font-weight:400;white-space:nowrap}
.follow p{font-size:8px;line-height:10px;margin-top:4px}
.social{display:flex;gap:6px;margin-top:6px}
.social i{display:block;width:16px;height:16px;border-radius:2px;background:#dce6cf}

/* footer */
.footer{left:0;top:1013px;width:878px;height:160px;background:var(--green)}
.footer-bar{left:0;top:1173px;width:878px;height:27px;background:var(--green-dark);color:var(--white);font-size:8px;text-align:center;padding-top:8px}
.f-title{font-size:10.5px;color:var(--white);padding-bottom:4px;border-bottom:1px dashed #b9cfa0;white-space:nowrap}
.links{left:119px;top:1023px;width:68px}
.links ul{list-style:none;margin-top:8px}
.links li{font-size:8.8px;color:var(--white);line-height:14.4px;white-space:nowrap}
.reviews-title{left:234px;top:1023px;width:90px}
.review-arrows{left:396px;top:1022px;color:var(--white);font-size:12px;letter-spacing:6px}
.review{left:234px;top:1049px;width:186px;height:91px;background:#a3bf82;border-radius:7px;color:var(--white);font-size:8.6px;line-height:12px;padding:8px}
.review-tail{left:246px;top:1140px}
.reviewer{left:234px;top:1149px;font-family:"Bitter",Georgia,serif;font-size:10px;color:var(--white)}
.inq-title{left:457px;top:1023px;width:80px}
.field{left:457px;width:135px;background:#a3bf82;border:1px solid #b2cb96;font-size:7.5px;font-style:italic;color:var(--white);padding:4px 8px}
.submit{left:457px;top:1144px;width:47px;height:17px;background:var(--green-deep);color:var(--white);font-size:9.5px;display:flex;align-items:center;justify-content:center;border-radius:2px}
.footer-brand{left:636px;top:1092px;font-family:"Bitter",Georgia,serif;font-weight:700;font-size:20px;color:#a8c28b;text-align:center;width:120px;line-height:22px}
</style>
</head>
<body>

<header>
  <div class="abs brand"><span class="brand-dot"></span>Lend a Lantern</div>
  <div class="abs btn-donate header-donate">DONATE NOW</div>
  <div class="abs phone">
    <svg width="22" height="22" viewBox="0 0 22 22"><circle cx="11" cy="11" r="10" fill="none" stroke="#7b9f4f" stroke-width="1.6"/><path d="M7.5 6.5c.8-.8 1.6-.6 2 .2l.8 1.6c.3.6 0 1.1-.5 1.5.6 1.3 1.5 2.2 2.8 2.8.4-.5.9-.8 1.5-.5l1.6.8c.8.4 1 1.2.2 2-1.4 1.4-3.7.7-5.6-1.2S6.1 7.9 7.5 6.5z" fill="#7b9f4f"/></svg>
    555-014-2368
  </div>
  <nav class="abs nav">
    <span class="current">&gt;Home&gt;</span><span>About Us</span><span>Training Programs</span><span>Photo &amp; Videos</span><span>Testimonials</span><span>Contact Us</span>
  </nav>
</header>

<section>
  <div class="abs hero-band"></div>
  <div class="abs hero-photo" role="img" aria-label="Photo of a coach holding a soccer ball and talking with a young player"></div>
  <div class="abs hero-caption">OUR MISSION: IMPROVE YOU WHILE IMPROVING SOMEONE ELSE
    <div class="abs hero-dots"><i></i><i></i><i></i><i></i></div>
  </div>
</section>

<section>
  <h2 class="abs h2 welcome-title">Welcome to <span class="dark">LEND A</span> <span class="muted">LANTERN</span></h2>
  <p class="abs welcome-text">Lorem ipsum dolor sit amet, consectetuer adipiscing elit, sed diam nonummy nibh euisiainciaadunt ut laoreet dolore magna aliquam erat volutpat. Ut wisi enim ad minim veniam, quigs nostruexerci taation ullamcorper suscipit lobortis nisl ut aliquip accumsan et iusto odio dvignissim qui blanditent luptreatum zzril delenit augue duis dolore te feugait nulla facilidolore magna aliquam erat volutpat. Ut wisi enim ad minim veniam, quis nostruexercadi tation ullamcorper suscipit lobortis nisl ut aliquip accumsan et iusto odio dignissim qui blanditent lure ptatum zzril delenit augue duis dolore te feugait nulla facilisi.......<b>read more &gt;&gt;</b></p>
  <p class="abs mission">We are nonprofit organization providing soccer training opportunities to youth soccer players looking to improve their game while also affecting the lives of the less fortunate in a positive way</p>

  <h2 class="abs h2 video-title">View <span class="muted">Video</span></h2>
  <div class="abs video" role="img" aria-label="Video of a coach talking with a youth soccer team">
    <div class="video-play"></div>
    <div class="video-bar"></div>
  </div>
</section>

<section>
  <div class="abs gallery"></div>
  <h2 class="abs h2 gallery-title">Photo <span class="muted">Gallery</span></h2>
  <div class="abs gallery-arrows">‹ ›</div>
  <div class="abs thumb" style="left:128px"><div role="img" aria-label="Coach with a young player and a ball" style="background:linear-gradient(135deg,#4d5a70,#b8a28f)"></div></div>
  <div class="abs thumb" style="left:253px"><div role="img" aria-label="Coach with players on a field at dusk" style="background:linear-gradient(#2f3a26,#55702f)"></div></div>
  <div class="abs thumb" style="left:379px"><div role="img" aria-label="Children in red kits sitting on grass" style="background:linear-gradient(#e9e9e0 40%,#7ea543)"></div></div>
  <div class="abs thumb" style="left:505px"><div role="img" aria-label="Coach with children in yellow kits" style="background:linear-gradient(#6e9a3c,#d8c43a)"></div></div>
  <div class="abs thumb" style="left:634px"><div role="img" aria-label="Team in yellow kits gathered on grass" style="background:linear-gradient(#9aad6a,#b9a83c)"></div></div>
</section>

<section>
  <div class="abs tab on" style="left:118px;width:88px">News &amp; Updates</div>
  <div class="abs tab" style="left:217px;width:85px">Upcoming Event</div>
  <div class="abs tab" style="left:313px;width:65px">Blog Posts</div>
  <div class="abs panel news">
    <div class="news-item"><div class="date">25/07/2014</div>Lorem ipsum dolor sit amet, consectetuer adipiscing elit, sed diam nonummy nibh euisiainciaadunt ut laoreet dolore magna aliquam erat volutpat.</div>
    <div class="news-item"><div class="date">20/07/2014</div>Lorem ipsum dolor sit amet, consectetuer adipiscing elit, sed diam nonummy nibh euisiainciaadunt ut laoreet dolore magna aliquam erat volutpat.</div>
    <div class="news-item"><div class="date">23/07/2014</div>Lorem ipsum dolor sit amet, consectetuer adipiscing elit, sed diam nonummy nibh euisiainciaadunt ut laoreet dolore magna aliquam erat volutpat.</div>
    <div class="dots"><i></i><i></i><i></i><i></i></div>
  </div>

  <div class="abs tab on" style="left:401px;width:60px">Directors</div>
  <div class="abs tab" style="left:473px;width:85px">Board Members</div>
  <div class="abs panel directors">
    <div class="person"><div class="avatar" role="img" aria-label="Director portrait"></div><p><span class="name">Mr. Lorem Ispim</span><br>Degree<br>Lorem Ispum</p></div>
    <div class="person"><div class="avatar" role="img" aria-label="Director portrait"></div><p><span class="name">Mr. Lorem Ispim</span><br>Degree<br>Lorem Ispum</p></div>
    <div class="person"><div class="avatar" role="img" aria-label="Director portrait"></div><p><span class="name">Mr. Lorem Ispim</span><br>Degree<br>Lorem Ispum</p></div>
    <div class="dots" style="right:10px"><i></i><i></i><i></i><i></i></div>
  </div>

  <div class="abs support-title">Help Support Our Cause</div>
  <div class="abs support">Join the Cause And<br>Make A Donation
    <div class="btn-donate">DONATE NOW</div>
  </div>
  <div class="abs support-shadow"></div>
  <div class="abs follow">
    <h3>Follow Lend a Lantern</h3>
    <p>Keep Up With Social Events<br>And Happenings</p>
    <div class="social"><i></i><i></i><i></i><i></i><i></i></div>
  </div>
</section>

<footer>
  <div class="abs footer"></div>
  <div class="abs links"><div class="f-title">Quick Links</div>
    <ul><li>Home</li><li>About Us</li><li>Packages</li><li>Photo &amp; Videos</li><li>Receptions</li><li>Testimonials</li><li>Contact Us</li></ul>
  </div>
  <div class="abs reviews-title"><div class="f-title">Client Reviews</div></div>
  <div class="abs review-arrows">‹ ›</div>
  <div class="abs review">"Lorem ipsum dolor sit amet, consectetuer adipiscing elit, sed diam nonummy nibh euisiainciaadunt ut laoreet dolore magna aliquam erat volutpat. Ut wisi enim ad minim veniam, quigs nostruexerci taation ullamcorper.........."</div>
  <svg class="abs review-tail" width="14" height="10" viewBox="0 0 14 10"><path d="M0 0h14L2 10z" fill="#a3bf82"/></svg>
  <div class="abs reviewer">Mara and Joel</div>
  <div class="abs inq-title"><div class="f-title">Quick Inquiry</div></div>
  <div class="abs field" style="top:1047px;height:19px">Name</div>
  <div class="abs field" style="top:1070px;height:19px">Email</div>
  <div class="abs field" style="top:1092px;height:49px">Message</div>
  <div class="abs submit">Submit</div>
  <div class="abs footer-brand">Lend a Lantern</div>
  <div class="abs footer-bar">Copyright © 2014 &nbsp;Lend a Lantern &nbsp;&nbsp;All Rights Reserved</div>
</footer>

</body>
</html>
```